Summer Music/Chorus/Choir Camp for Young Singers Ages 8-13

We need a flyer for a summer camp for young singers ages 8-13. We are nonprofit community children's chorus in Miami, FL. Our camp provides specialized training in music theory, sight-reading,and aural training through daily choral rehearsals in an environment that is both positive and a lot of fun! Our camp offers children the opportunity to come as they are, no matter the level of experience, and grow tremendously in their musicianship skills. In addition to this, our campers participate in song-writing, masterclasses, community performances, and media projects. The final design should be clean, fun, not too crowded, should appeal to boys and girls ages 8-13, and something someone that age would consider "cool" and not too childish. Drawings are cool, something different.
Updates

Target Market(s)

Ages 8-13 and parents of those kids.

Industry/Entity Type

Community

Requirements
Must have
• All info attached.
Nice to have
• Things that relate to music, especially related to singing/choirs
Should not have
• instruments, stock photos of children, or photos from our website (unless they are used very creatively), or photos in general. I've attached our previous camp flyer and our current organization flyer but I don't necessarily want this flyer to look like those.

```html
<!DOCTYPE html>
<html lang="en">
<head>
<meta charset="utf-8">
<title>Summer Choral Camp 2016</title>
<link rel="stylesheet" href="https://fonts.googleapis.com/css2?family=Oswald:wght@600;700&family=Roboto+Condensed:wght@400;700&family=Roboto:ital,wght@0,400;0,700;1,400&display=swap">
<style>
  :root {
    --page: #e9e9e9;
    --flyer: #000000;
    --band: #0b0d0e;
    --mint: #a9d8d3;
    --teal-logo: #4f8a86;
    --note: #5fc6dc;
    --note-deep: #3fa7c1;
    --ink: #111111;
    --white: #ffffff;
    --orange: #f7a21b;
    --green: #3fae6a;
    --cyan: #1aa0d8;
    --indigo: #2e3a9a;
  }
  * { box-sizing: border-box; margin: 0; padding: 0; }
  html, body { width: 1006px; height: 1200px; overflow: hidden; background: var(--page); }
  .flyer {
    position: relative; width: 1006px; height: 1200px;
    background: var(--flyer); overflow: hidden;
    font-family: "Roboto", Arial, sans-serif; color: var(--white);
  }
  .backdrop-band {
    position: absolute; left: 0; top: 255px; width: 1006px; height: 690px;
    background: var(--band);
  }
  .camp-title {
    position: absolute; top: 62px; left: 0; width: 100%;
    text-align: center; font-family: "Oswald", "Arial Narrow", sans-serif;
    font-weight: 700; font-size: 104px; line-height: 1; letter-spacing: -1px;
    word-spacing: -6px;
    background: linear-gradient(90deg, var(--orange) 0%, #e8a020 28%, #8fa640 42%, var(--green) 55%, var(--cyan) 75%, var(--indigo) 100%);
    -webkit-background-clip: text; background-clip: text; color: transparent;
    text-transform: uppercase;
  }
  .camp-year {
    position: absolute; top: 188px; left: 0; width: 100%; text-align: center;
    font-family: "Roboto Condensed", Arial, sans-serif; font-weight: 700;
    font-size: 56px; color: var(--mint);
  }
  .camp-year .star { font-size: 30px; vertical-align: middle; margin: 0 18px; }
  .equalizer {
    position: absolute; left: 28px; top: 290px; width: 950px; height: 230px;
    background: linear-gradient(90deg, #e5202a 0%, #f39a1f 18%, #f2e31c 32%, #3fbf55 45%, #27b7a8 58%, #2a8fe0 70%, #4438b8 84%, #9b2fb5 100%);
    -webkit-mask-image: linear-gradient(0deg, #000 0%, rgba(0,0,0,.75) 45%, rgba(0,0,0,0) 100%);
    mask-image: linear-gradient(0deg, #000 0%, rgba(0,0,0,.75) 45%, rgba(0,0,0,0) 100%);
  }
  .equalizer-reflection {
    position: absolute; left: 28px; top: 520px; width: 950px; height: 110px;
    background: linear-gradient(90deg, #e5202a 0%, #f39a1f 18%, #f2e31c 32%, #3fbf55 45%, #27b7a8 58%, #2a8fe0 70%, #4438b8 84%, #9b2fb5 100%);
    opacity: .35;
    -webkit-mask-image: linear-gradient(180deg, #000 0%, rgba(0,0,0,0) 100%);
    mask-image: linear-gradient(180deg, #000 0%, rgba(0,0,0,.0) 100%);
  }
  .chorus-name {
    position: absolute; left: 58px; top: 640px; width: 430px;
    font-family: "Roboto Condensed", Arial, sans-serif; font-weight: 700;
    color: var(--teal-logo); font-size: 44px; line-height: 1.1;
    display: flex; align-items: center; gap: 16px;
  }
  .chorus-name .mark { width: 22px; height: 22px; background: var(--teal-logo); flex: none; }
  .camp-blurb {
    position: absolute; left: 45px; top: 836px; width: 412px;
    font-family: "Roboto Condensed", Arial, sans-serif; font-size: 19.5px; line-height: 26px;
    text-align: justify; hyphens: auto;
  }
  .details-note {
    position: absolute; left: 540px; top: 560px; width: 410px; height: 385px;
    background: linear-gradient(180deg, var(--note) 0%, #56bdd6 75%, var(--note-deep) 100%);
    transform: rotate(-2.6deg);
    box-shadow: 0 6px 14px rgba(0,0,0,.55);
    color: var(--ink); font-family: "Roboto Condensed", Arial, sans-serif;
    text-align: center; padding-top: 78px;
  }
  .details-note .dates { font-size: 31px; font-weight: 400; letter-spacing: .2px; }
  .details-note .small { font-size: 17px; line-height: 24px; }
  .details-note .venue { font-size: 22px; line-height: 27px; margin-top: 42px; }
  .details-note .price { font-size: 23px; margin-top: 36px; }
  .details-note .fine { font-size: 14px; }
  .contact {
    position: absolute; left: 540px; top: 960px; width: 410px; text-align: center;
    font-family: "Roboto Condensed", Arial, sans-serif; font-weight: 700;
  }
  .contact .phone { font-family: "Roboto", Arial, sans-serif; font-size: 45px; color: var(--mint); letter-spacing: 1px; }
  .contact .web { font-size: 23px; line-height: 26px; margin-top: 10px; }
  .nonprofit-note {
    position: absolute; left: 20px; top: 1122px; width: 470px; text-align: center;
    font-style: italic; font-size: 15.5px; line-height: 19px;
  }
  .partner-badges { position: absolute; left: 505px; top: 1120px; display: flex; gap: 8px; align-items: center; }
  .badge { background: var(--white); height: 50px; }
  .badge.wide { width: 95px; }
  .badge.square { width: 50px; }
  .badge.long { width: 275px; }
</style>
</head>
<body>
<main class="flyer">
  <div class="backdrop-band"></div>
  <h1 class="camp-title">Summer Choral Camp</h1>
  <p class="camp-year"><span class="star">★</span>2016<span class="star">★</span></p>

  <div class="equalizer" role="img" aria-label="Rainbow sound equalizer bars"></div>
  <div class="equalizer-reflection" aria-hidden="true"></div>

  <p class="chorus-name"><span class="mark"></span>The Young Voices Chorus</p>

  <p class="camp-blurb">Youth and children who love to sing will have a blast at our choral camp! Our music educators and industry professionals are dedicated to enhancing the lives of young singers through choral training which develops vocal technique, ear-training, music reading, and interpersonal skills. Activities are fun and interactive and former music training is not necessary. Singers in grades 3-9 are invited to attend! Register today!</p>

  <section class="details-note">
    <p class="dates">July 18-29, 9am-3pm (M-F)*</p>
    <p class="small">*Extended hours available (7:30am-5:30pm)<br>for an extra $50 per week.</p>
    <p class="venue">Southbay Community Arts Hall,<br>4820 Harmony Lane<br>Coral Bay, FL 33000</p>
    <p class="price">*$300 for two-week session</p>
    <p class="fine">*Price does not include lunch</p>
  </section>

  <section class="contact">
    <p class="phone">555.014.2290</p>
    <p class="web">hello@youngvoiceschorus.org<br>youngvoiceschorus.org</p>
  </section>

  <p class="nonprofit-note">The Young Voices is a 501 (c)(3) Nonprofit organization.<br>Donations made to YVC are tax-exempt</p>

  <div class="partner-badges" aria-label="Partner badges">
    <div class="badge wide"></div>
    <div class="badge square"></div>
    <div class="badge long"></div>
  </div>
</main>
</body>
</html>
```